Corkly Soy Candles - New WP TEMPLATE

We make handemade soy candles in large volume and our company is now seeing huge growth, we are about to break into the retail market by providing our candles wholesale to retail outlets and gift stores.

Our candles are set apart by the fact they are very earth friendly in the sense of utilising old wine bottles that are cut in half and filling them with highly scented all natural pure soy and sealing the candle with a cork.

The website will need to be a complete Wordpress template. PLEASE ensure it is responsive and mobile friendly.

The look and feel of the website will need to be very original and rustic in feel.

Some examples of the "feel" of the site cand be found at the following links:

http://www.example-plankstudio.test/blog/2011/07/new-website-launches-for-july/

http://www.example-fernhutcabin.test/

http://www.example-glowvatlights.test/

http://www.example-sage417.test/wedding-logo/rustic-ombre-summer-wedding-website/

http://example-plumthemes.test/grunge-website-design/screen-shot-2012-02-04-at-6-22-21-pm/

Our lettering logo is simply the word "Corkly" in the font "Sweetly Broken". I have included our WORD logo and our SYMBOL logo. You will see our product in the images attached.

The site should include:

A slider
All images to be in circle cut outs (not square)

-A homepage with slider
-A section for "The Story" (This will be the largest page with a circle for each of the 6 scents and then a staggered story line of how we make the candles, alternating pictures from left to right).
-A section for "Retailers"
-A section for "Wholesale"
-A contact section

Please place some sort of placeholder images in all of the areas that will have images - were having the images done professionally and I have some design experience so I can finalise this aspect.

If you can make this a "One page template" that would be okay, but we are also open to multipage designs as long as its user friendly.

See images for the process and feel of product.

IF you think the prize needs to be increased and you have a good design that we like, we are happy to negotiate with you!

```html
<!DOCTYPE html>
<html lang="en">
<head>
<meta charset="utf-8">
<title>Corkly Soy Candles</title>
<link href="https://fonts.googleapis.com/css2?family=Arvo&family=Open+Sans:wght@400;700&family=Dancing+Script:wght@500&display=swap" rel="stylesheet">
<style>
:root{
  --wood-light:#d9a76b;
  --wood-mid:#c28a4e;
  --wood-dark:#a56e37;
  --parchment:#f3e7c8;
  --oval:#f1dfa4;
  --brand-brown:#6e3d1c;
  --panel-gray:#e4e3e1;
  --band-brown:#854819;
  --caption:#f6e6cc;
  --footer:#333333;
  --footer-line:#1c1c1c;
  --footer-text:#ffffff;
  --footer-muted:#bdbdbd;
  --button-gray:#575757;
  --button-cream:#f2e3b0;
  --nav-text:#6b5a48;
  --body-text:#3c3c3c;
}
*{margin:0;padding:0;box-sizing:border-box}
html,body{width:1067px;height:1200px;overflow:hidden}
body{position:relative;font-family:"Open Sans",Arial,sans-serif;background:var(--wood-mid)}
.wood-backdrop{position:absolute;left:0;top:0;width:1067px;height:1027px;
  background:linear-gradient(180deg,var(--wood-light) 0%,var(--wood-mid) 45%,var(--wood-light) 75%,var(--wood-mid) 100%)}
.hanger{position:absolute;top:0;width:3px;height:40px;background:#2b2219}
.logo-oval{position:absolute;left:390px;top:28px;width:267px;height:105px;border-radius:50%;background:var(--oval);
  display:flex;align-items:center;justify-content:center}
.logo-name{font-family:"Dancing Script",cursive;font-weight:500;font-size:44px;color:var(--brand-brown)}
.cart-button{position:absolute;left:827px;top:71px;width:151px;height:39px;border-radius:5px;background:#7a4a22;
  border:2px solid #b07a3c;display:flex;align-items:center;justify-content:center;gap:8px;
  font-family:"Arvo",serif;font-size:14px;color:var(--oval)}
.main-nav{position:absolute;left:89px;top:151px;width:887px;height:43px;background:var(--parchment);
  box-shadow:0 2px 4px rgba(0,0,0,.25)}
.main-nav .rivet{position:absolute;top:18px;width:7px;height:7px;border-radius:50%;background:#2a2420}
.main-nav a{position:absolute;top:12px;font-family:"Arvo",serif;font-size:13.5px;letter-spacing:.5px;color:var(--nav-text);text-decoration:none}
.slider-frame{position:absolute;left:89px;top:218px;width:887px;height:400px;background:var(--parchment);
  box-shadow:0 3px 6px rgba(0,0,0,.35)}
.slider-photo{position:absolute;left:10px;top:10px;width:867px;height:381px;
  background:linear-gradient(180deg,#6d6a55 0%,#c9c3a8 30%,#b7ad7c 55%,#5a3a2c 80%,#4a2e24 100%)}
.story-panel{position:absolute;left:89px;top:620px;width:889px;height:220px;background:var(--panel-gray)}
.story-title{position:absolute;left:0;width:100%;top:24px;text-align:center;font-weight:700;font-size:21px;letter-spacing:.5px;color:#1d1d1d}
.story-text{position:absolute;left:98px;width:720px;top:57px;text-align:center;font-size:12.5px;line-height:16px;color:var(--body-text)}
.story-band{position:absolute;left:89px;top:840px;width:889px;height:129px;background:var(--band-brown);
  box-shadow:0 3px 5px rgba(0,0,0,.3)}
.scent{position:absolute;top:739px;width:160px;text-align:center}
.scent-photo{width:154px;height:154px;margin:0 auto;border-radius:50%;border:5px solid #fff;box-shadow:0 2px 4px rgba(0,0,0,.3)}
.scent-name{margin-top:10px;font-size:21px;color:var(--caption)}
.site-footer{position:absolute;left:0;top:1027px;width:1067px;height:173px;background:var(--footer)}
.advertise{position:absolute;left:412px;top:18px;width:316px;height:35px;border-radius:4px;overflow:hidden;display:flex}
.advertise-label{flex:1;background:var(--button-gray);color:#f0f0f0;font-weight:700;font-size:16px;letter-spacing:.5px;padding:7px 0 0 27px}
.advertise-action{width:74px;background:var(--button-cream);color:#333;font-weight:700;font-size:8px;text-decoration:underline;
  display:flex;align-items:center;justify-content:center}
.footer-rule{position:absolute;left:126px;top:72px;width:809px;height:3px;background:var(--footer-line)}
.footer-nav{position:absolute;left:134px;top:98px;font-size:11.5px;color:var(--footer-text)}
.footer-nav span{margin:0 9px}
.copyright{position:absolute;left:134px;top:119px;font-size:11px;color:var(--footer-muted)}
.social{position:absolute;top:102px;width:25px;height:25px;border-radius:50%;background:#fff}
</style>
</head>
<body>
<div class="wood-backdrop" role="img" aria-label="Rustic light wood plank background"></div>

<div class="hanger" style="left:467px"></div>
<div class="hanger" style="left:559px"></div>
<div class="logo-oval"><span class="logo-name">Corkly</span></div>

<div class="cart-button">Shopping Cart
  <svg width="20" height="18" viewBox="0 0 20 18" fill="none" stroke="#f1dfa4" stroke-width="1.5">
    <path d="M1 2h3l2 10h10l2-7H5"/><circle cx="8" cy="15.5" r="1.3"/><circle cx="15" cy="15.5" r="1.3"/>
  </svg>
</div>

<nav class="main-nav">
  <span class="rivet" style="left:13px"></span>
  <a href="#" style="left:58px">HOME</a>
  <a href="#" style="left:152px">ABOUT US</a>
  <a href="#" style="left:269px">SERVICES</a>
  <a href="#" style="left:386px">CONTACT US</a>
  <span class="rivet" style="left:870px"></span>
</nav>

<div class="slider-frame">
  <div class="slider-photo" role="img" aria-label="Slider photo of wine bottle soy candles with cork labels on a granite counter"></div>
</div>

<section class="story-panel">
  <h2 class="story-title">OUR STORY</h2>
  <p class="story-text">Lorem Ipsum is simply dummy text of the printing and typesetting industry. Lorem Ipsum has been the industry's standard dummy text ever since the 1500s, when an unknown printer took a galley of type and scrambled it to make a type specimen book. It has survived not only five</p>
</section>
<div class="story-band"></div>

<div class="scent" style="left:206px">
  <div class="scent-photo" role="img" aria-label="Cut glass bottle candle jars with wicks" style="background:linear-gradient(135deg,#2f4a3a,#8fb0a0,#4c6a3a)"></div>
  <div class="scent-name">Lorem Ipsum</div>
</div>
<div class="scent" style="left:443px">
  <div class="scent-photo" role="img" aria-label="Rows of corked candle tops" style="background:linear-gradient(135deg,#7a5a48,#d9a58a,#b98468)"></div>
  <div class="scent-name">Lorem Ipsum</div>
</div>
<div class="scent" style="left:667px">
  <div class="scent-photo" role="img" aria-label="Finished candles lined up on a shelf" style="background:linear-gradient(135deg,#3a5a78,#c8c6b0,#5e6a3a)"></div>
  <div class="scent-name">Lorem Ipsum</div>
</div>

<footer class="site-footer">
  <div class="advertise">
    <div class="advertise-label">ADVERTISE WITH US</div>
    <div class="advertise-action">Click Here</div>
  </div>
  <div class="footer-rule"></div>
  <div class="footer-nav">HOME<span>|</span>ABOUT<span>|</span>MEMBERS<span>|</span>CANDLES<span>|</span>EVENTS<span>|</span>MEMBERSHIP<span>|</span>CONTACT</div>
  <div class="copyright">Copyright © 2014 Hollowmere. All Rights Reserved</div>
  <span class="social" style="left:829px"></span>
  <span class="social" style="left:857px"></span>
  <span class="social" style="left:886px"></span>
  <span class="social" style="left:914px"></span>
</footer>
</body>
</html>
```